Re-design a website for a millionaire mentor

We need an expert website designer to re-design the website vKeenstride.net

The website would have 4 pages. A home page, Summit Circle page, Hire RM page and an About page.

Here are some reference websites

https://www.lumovance.net
https://rolfbanter.net/

I will also attach a beginning of mockup of the home page I did myself to give an idea of the style we like, please use the quote "If you are not chasing your potential you are wasting your life" instead of the one in the current website...

You don't have the use the mockup (just the quote) and are free to use all your creativity.

Target Market(s)

Entrepreneurs

Number of Pages Required

4 page

Font styles to use
Other font styles liked:
• Franklin Gothic

Requirements
Must have
• -Call of action on the main page to download a free business plan
• -Hire rm page check out reference: http://www.hiremarkbellow.net
• -summit circle page with a button to sign in or join the summit circle. Check out reference for example: https://www.lumovance.net/glide_academy

```html
<!DOCTYPE html>
<html lang="en">
<head>
<meta charset="utf-8">
<title>Hire Rex Marlowe</title>
<link rel="stylesheet" href="https://fonts.googleapis.com/css2?family=Jost:wght@400;500&family=Barlow:wght@300;400&display=swap">
<style>
  :root {
    --page-dim: #2b2b2b;
    --header-dim: #3a3a3a;
    --foliage-dark: #1c2418;
    --foliage-mid: #2f3a28;
    --modal-bg: #ffffff;
    --ink: #111111;
    --label: #3c3c3c;
    --field-border: #c9c9c9;
    --accent: #48d0a0;
    --accent-text: #ffffff;
  }
  * { box-sizing: border-box; margin: 0; padding: 0; }
  html, body {
    width: 1200px;
    height: 530px;
    overflow: hidden;
    background: var(--page-dim);
  }
  .canvas {
    position: relative;
    width: 1200px;
    height: 530px;
    overflow: hidden;
  }
  .site-header {
    position: absolute;
    left: 0; top: 0;
    width: 1200px; height: 46px;
    background: var(--header-dim);
  }
  .hero-backdrop {
    position: absolute;
    left: 0; top: 46px;
    width: 1200px; height: 484px;
    background: radial-gradient(ellipse at 20% 40%, var(--foliage-mid), var(--foliage-dark) 70%);
  }
  .booking-modal {
    position: absolute;
    left: 97px; top: 3px;
    width: 1001px; height: 527px;
    background: var(--modal-bg);
  }
  .modal-close {
    position: absolute;
    left: 952px; top: 24px;
    width: 24px; height: 24px;
  }
  .brand {
    position: absolute;
    left: 0; top: 66px;
    width: 100%;
    display: flex;
    justify-content: center;
    align-items: center;
    gap: 8px;
    font-family: "Jost", sans-serif;
    font-weight: 500;
    font-size: 20px;
    letter-spacing: 1px;
    color: var(--ink);
  }
  .brand-mark {
    width: 16px; height: 16px;
    background: var(--ink);
  }
  .modal-title {
    position: absolute;
    left: 0; top: 143px;
    width: 100%;
    text-align: center;
    font-family: "Jost", sans-serif;
    font-weight: 500;
    font-size: 54px;
    letter-spacing: 4.5px;
    color: var(--ink);
    line-height: 1;
  }
  .contact-row {
    position: absolute;
    left: 0; top: 214px;
    width: 100%;
    display: flex;
    justify-content: center;
    align-items: center;
    gap: 22px;
    font-family: "Jost", sans-serif;
    font-size: 17px;
    color: var(--ink);
    white-space: nowrap;
  }
  .social-links {
    display: flex;
    gap: 8px;
    font-size: 13px;
    font-weight: 500;
  }
  .booking-form {
    position: absolute;
    left: 0; top: 0;
    width: 100%; height: 100%;
    font-family: "Barlow", sans-serif;
  }
  .field-label {
    position: absolute;
    width: 130px;
    left: 224px;
    text-align: right;
    font-weight: 300;
    font-size: 17px;
    letter-spacing: 0.5px;
    color: var(--label);
  }
  .field-input {
    position: absolute;
    left: 372px;
    width: 451px;
    border: 1px solid var(--field-border);
    border-radius: 5px;
    background: var(--modal-bg);
    box-shadow: 0 1px 3px rgba(0,0,0,0.35);
    resize: none;
  }
  .label-name { top: 240px; }
  .input-name { top: 239px; height: 37px; }
  .label-email { top: 288px; }
  .input-email { top: 287px; height: 37px; }
  .label-message { top: 335px; }
  .input-message { top: 332px; height: 147px; }
  .submit-button {
    position: absolute;
    left: 765px; top: 487px;
    width: 58px; height: 38px;
    border: none;
    border-radius: 5px;
    background: var(--accent);
    color: var(--accent-text);
    font-family: "Barlow", sans-serif;
    font-size: 18px;
    letter-spacing: 0.5px;
  }
</style>
</head>
<body>
<div class="canvas">
  <div class="site-header"></div>
  <div class="hero-backdrop" role="img" aria-label="Dimmed photograph of dense green foliage behind the booking window"></div>

  <section class="booking-modal">
    <svg class="modal-close" viewBox="0 0 24 24" aria-label="Close">
      <path d="M1 1 L23 23 M23 1 L1 23" stroke="#111" stroke-width="1.6" fill="none"/>
    </svg>

    <div class="brand"><span class="brand-mark"></span><span>KEEN STRIDE</span></div>

    <h1 class="modal-title">Hire Rex Marlowe</h1>

    <div class="contact-row">
      <div class="social-links">
        <span>Loop</span><span>Chirp</span><span>Frame</span>
      </div>
      <span>Tel: 555-014-2286 &nbsp;|&nbsp; Fax: 555-014-2287 &nbsp;|&nbsp; hello@keenstride.net</span>
    </div>

    <form class="booking-form">
      <label class="field-label label-name" for="name">Name *</label>
      <input class="field-input input-name" id="name" type="text">
      <label class="field-label label-email" for="email">Email *</label>
      <input class="field-input input-email" id="email" type="email">
      <label class="field-label label-message" for="message">Message</label>
      <textarea class="field-input input-message" id="message"></textarea>
      <button class="submit-button" type="button">BOOK</button>
    </form>
  </section>
</div>
</body>
</html>
```